Design für einen Jahresplaner gesucht
Zielgruppe
Scannen und Designen Zahntechnischer und Zahnmedizinischer Arbeiten und das Fräsen und 3d Drucken von bereits in CAD konstruierten Objekten. Wir verfügen über die modernsten Zahntechnischen Technologien und bieten diese als Dienstleister für Dentallabore an.
Aufgabenstellung
Wir benotigen ein Jahresplaner für unsere Kunden. Die Beigefügte Vorlage dient regelrecht nur der Grösenvorlage.
Das Design soll Technisch und Innovativ sein. Gleischzeitig aber gradlinig und nicht zu verspielt.
Das Logo kann ruhig stark ins Auge fallen. Die Schriftfarben sollen überwigen dunkelgrau sein. Hervorzuhebende Bereiche wie z. B. Sonntage, Feiertage sollten die Logofaben beinhalten. Bilder können auch verwendet werden aber wir würden uns über ein Schönes Layout ohne Bilder auch freuen.
PS: Unter dem Logo muss in Feiner Schrift stehen
eine Marke der Norvak GmbH

```html
<!DOCTYPE html>
<html lang="de">
<head>
<meta charset="utf-8">
<title>Jahresplaner 2019</title>
<link href="https://fonts.googleapis.com/css2?family=Poppins:wght@300;400;500;600;700&display=swap" rel="stylesheet">
<style>
:root{
  --paper:#f4f6f9;
  --ink:#4a4a4a;
  --ink-soft:#777;
  --title:#5f5f5f;
  --rule:#8a8a8a;
  --month:#a9d4ea;
  --weekend:#fde8c3;
  --holiday:#b1186e;
}
*{margin:0;padding:0;box-sizing:border-box}
html,body{width:1200px;height:870px;overflow:hidden;background:var(--paper);font-family:"Poppins",sans-serif;color:var(--ink)}
.planner{position:relative;width:1200px;height:870px}
.brand{position:absolute;left:94px;top:44px;display:flex;flex-direction:column}
.brand-row{display:flex;align-items:center;gap:10px}
.brand-dot{width:34px;height:34px;border-radius:50%;background:var(--holiday)}
.brand-name{font-size:38px;font-weight:600;color:var(--title);letter-spacing:.5px;line-height:1}
.brand-sub{font-size:8.5px;font-weight:300;color:var(--ink-soft);margin:4px 0 0 44px}
.title{position:absolute;left:392px;top:48px;font-size:42px;font-weight:700;color:var(--title);letter-spacing:.5px;line-height:1}
.months{position:absolute;left:94px;top:125px;display:grid;grid-template-columns:repeat(12,73px);column-gap:13.6px}
.month h2{height:24px;background:var(--month);border-radius:4px 4px 0 0;color:#fff;font-size:10.5px;font-weight:600;text-align:center;line-height:26px;letter-spacing:.3px;margin-bottom:3px}
.month ol{list-style:none}
.month li{position:relative;height:21.4px;border-bottom:.8px solid var(--rule);padding:2px 0 0 2px}
.month li.s{background:var(--weekend)}
.month li b{display:block;font-size:9px;font-weight:600;line-height:10px;color:var(--ink)}
.month li.h b{color:var(--holiday)}
.month li i{display:block;font-style:normal;font-size:4.3px;line-height:6px;color:var(--ink-soft);white-space:nowrap;overflow:hidden}
.month li em{position:absolute;right:1px;bottom:2px;font-style:normal;font-size:6px;color:var(--ink-soft)}
.footer{position:absolute;left:0;right:0;top:832px;text-align:center;font-size:8.5px;color:var(--ink)}
</style>
</head>
<body>
<main class="planner">
  <header>
    <div class="brand">
      <div class="brand-row"><span class="brand-dot"></span><span class="brand-name">Dentora</span></div>
      <span class="brand-sub">eine Marke der Norvak GmbH</span>
    </div>
    <h1 class="title">2019 JAHRESPLANER</h1>
  </header>

  <section class="months">
    <div class="month"><h2>JANUAR</h2><ol>
      <li class="h"><b>1</b><i>DI · NEUJAHR</i></li><li><b>2</b><i>MI</i></li><li><b>3</b><i>DO</i></li><li><b>4</b><i>FR</i></li><li class="s"><b>5</b><i>SA</i></li><li class="s"><b>6</b><i>SO</i></li>
      <li><b>7</b><i>MO</i><em>2</em></li><li><b>8</b><i>DI</i></li><li><b>9</b><i>MI</i></li><li><b>10</b><i>DO</i></li><li><b>11</b><i>FR</i></li><li class="s"><b>12</b><i>SA</i></li><li class="s"><b>13</b><i>SO</i></li>
      <li><b>14</b><i>MO</i><em>3</em></li><li><b>15</b><i>DI</i></li><li><b>16</b><i>MI</i></li><li><b>17</b><i>DO</i></li><li><b>18</b><i>FR</i></li><li class="s"><b>19</b><i>SA</i></li><li class="s"><b>20</b><i>SO</i></li>
      <li><b>21</b><i>MO</i><em>4</em></li><li><b>22</b><i>DI</i></li><li><b>23</b><i>MI</i></li><li><b>24</b><i>DO</i></li><li><b>25</b><i>FR</i></li><li class="s"><b>26</b><i>SA</i></li><li class="s"><b>27</b><i>SO</i></li>
      <li><b>28</b><i>MO</i><em>5</em></li><li><b>29</b><i>DI</i></li><li><b>30</b><i>MI</i></li><li><b>31</b><i>DO</i></li>
    </ol></div>

    <div class="month"><h2>FEBRUAR</h2><ol>
      <li><b>1</b><i>FR</i></li><li class="s"><b>2</b><i>SA</i></li><li class="s"><b>3</b><i>SO</i></li>
      <li><b>4</b><i>MO</i><em>6</em></li><li><b>5</b><i>DI</i></li><li><b>6</b><i>MI</i></li><li><b>7</b><i>DO</i></li><li><b>8</b><i>FR</i></li><li class="s"><b>9</b><i>SA</i></li><li class="s"><b>10</b><i>SO</i></li>
      <li><b>11</b><i>MO</i><em>7</em></li><li><b>12</b><i>DI</i></li><li><b>13</b><i>MI</i></li><li><b>14</b><i>DO</i></li><li><b>15</b><i>FR</i></li><li class="s"><b>16</b><i>SA</i></li><li class="s"><b>17</b><i>SO</i></li>
      <li><b>18</b><i>MO</i><em>8</em></li><li><b>19</b><i>DI</i></li><li><b>20</b><i>MI</i></li><li><b>21</b><i>DO</i></li><li><b>22</b><i>FR</i></li><li class="s"><b>23</b><i>SA</i></li><li class="s"><b>24</b><i>SO</i></li>
      <li><b>25</b><i>MO</i><em>9</em></li><li><b>26</b><i>DI</i></li><li><b>27</b><i>MI</i></li><li><b>28</b><i>DO</i></li>
    </ol></div>

    <div class="month"><h2>MÄRZ</h2><ol>
      <li><b>1</b><i>FR</i></li><li class="s"><b>2</b><i>SA</i></li><li class="s"><b>3</b><i>SO</i></li>
      <li><b>4</b><i>MO</i><em>10</em></li><li><b>5</b><i>DI</i></li><li><b>6</b><i>MI</i></li><li><b>7</b><i>DO</i></li><li><b>8</b><i>FR</i></li><li class="s"><b>9</b><i>SA</i></li><li class="s"><b>10</b><i>SO</i></li>
      <li><b>11</b><i>MO</i><em>11</em></li><li><b>12</b><i>DI</i></li><li><b>13</b><i>MI</i></li><li><b>14</b><i>DO</i></li><li><b>15</b><i>FR</i></li><li class="s"><b>16</b><i>SA</i></li><li class="s"><b>17</b><i>SO</i></li>
      <li><b>18</b><i>MO</i><em>12</em></li><li><b>19</b><i>DI</i></li><li><b>20</b><i>MI</i></li><li><b>21</b><i>DO</i></li><li><b>22</b><i>FR</i></li><li class="s"><b>23</b><i>SA</i></li><li class="s"><b>24</b><i>SO</i></li>
      <li><b>25</b><i>MO</i><em>13</em></li><li><b>26</b><i>DI</i></li><li><b>27</b><i>MI</i></li><li><b>28</b><i>DO</i></li><li><b>29</b><i>FR</i></li><li class="s"><b>30</b><i>SA</i></li><li class="s"><b>31</b><i>SO</i></li>
    </ol></div>

    <div class="month"><h2>APRIL</h2><ol>
      <li><b>1</b><i>MO</i><em>14</em></li><li><b>2</b><i>DI</i></li><li><b>3</b><i>MI</i></li><li><b>4</b><i>DO</i></li><li><b>5</b><i>FR</i></li><li class="s"><b>6</b><i>SA</i></li><li class="s"><b>7</b><i>SO</i></li>
      <li><b>8</b><i>MO</i><em>15</em></li><li><b>9</b><i>DI</i></li><li><b>10</b><i>MI</i></li><li><b>11</b><i>DO</i></li><li><b>12</b><i>FR</i></li><li class="s"><b>13</b><i>SA</i></li><li class="s"><b>14</b><i>SO</i></li>
      <li><b>15</b><i>MO</i><em>16</em></li><li><b>16</b><i>DI</i></li><li><b>17</b><i>MI</i></li><li><b>18</b><i>DO</i></li><li class="h"><b>19</b><i>FR · KARFREITAG</i></li><li class="s"><b>20</b><i>SA</i></li><li class="s"><b>21</b><i>SO</i></li>
      <li class="h"><b>22</b><i>MO · OSTERMONTAG</i><em>17</em></li><li><b>23</b><i>DI</i></li><li><b>24</b><i>MI</i></li><li><b>25</b><i>DO</i></li><li><b>26</b><i>FR</i></li><li class="s"><b>27</b><i>SA</i></li><li class="s"><b>28</b><i>SO</i></li>
      <li><b>29</b><i>MO</i><em>18</em></li><li><b>30</b><i>DI</i></li>
    </ol></div>

    <div class="month"><h2>MAI</h2><ol>
      <li class="h"><b>1</b><i>MI · TAG DER ARBEIT</i></li><li><b>2</b><i>DO</i></li><li><b>3</b><i>FR</i></li><li class="s"><b>4</b><i>SA</i></li><li class="s"><b>5</b><i>SO</i></li>
      <li><b>6</b><i>MO</i><em>19</em></li><li><b>7</b><i>DI</i></li><li><b>8</b><i>MI</i></li><li><b>9</b><i>DO</i></li><li><b>10</b><i>FR</i></li><li class="s"><b>11</b><i>SA</i></li><li class="s"><b>12</b><i>SO</i></li>
      <li><b>13</b><i>MO</i><em>20</em></li><li><b>14</b><i>DI</i></li><li><b>15</b><i>MI</i></li><li><b>16</b><i>DO</i></li><li><b>17</b><i>FR</i></li><li class="s"><b>18</b><i>SA</i></li><li class="s"><b>19</b><i>SO</i></li>
      <li><b>20</b><i>MO</i><em>21</em></li><li><b>21</b><i>DI</i></li><li><b>22</b><i>MI</i></li><li><b>23</b><i>DO</i></li><li><b>24</b><i>FR</i></li><li class="s"><b>25</b><i>SA</i></li><li class="s"><b>26</b><i>SO</i></li>
      <li><b>27</b><i>MO</i><em>22</em></li><li><b>28</b><i>DI</i></li><li><b>29</b><i>MI</i></li><li class="h"><b>30</b><i>DO · CHRISTI HIMMELFAHRT</i></li><li><b>31</b><i>FR</i></li>
    </ol></div>

    <div class="month"><h2>JUNI</h2><ol>
      <li class="s"><b>1</b><i>SA</i></li><li class="s"><b>2</b><i>SO</i></li>
      <li><b>3</b><i>MO</i><em>23</em></li><li><b>4</b><i>DI</i></li><li><b>5</b><i>MI</i></li><li><b>6</b><i>DO</i></li><li><b>7</b><i>FR</i></li><li class="s"><b>8</b><i>SA</i></li><li class="h"><b>9</b><i>SO · PFINGSTSONNTAG</i></li>
      <li class="h"><b>10</b><i>MO · PFINGSTMONTAG</i><em>24</em></li><li><b>11</b><i>DI</i></li><li><b>12</b><i>MI</i></li><li><b>13</b><i>DO</i></li><li><b>14</b><i>FR</i></li><li class="s"><b>15</b><i>SA</i></li><li class="s"><b>16</b><i>SO</i></li>
      <li><b>17</b><i>MO</i><em>25</em></li><li><b>18</b><i>DI</i></li><li><b>19</b><i>MI</i></li><li><b>20</b><i>DO</i></li><li><b>21</b><i>FR</i></li><li class="s"><b>22</b><i>SA</i></li><li class="s"><b>23</b><i>SO</i></li>
      <li><b>24</b><i>MO</i><em>26</em></li><li><b>25</b><i>DI</i></li><li><b>26</b><i>MI</i></li><li><b>27</b><i>DO</i></li><li><b>28</b><i>FR</i></li><li class="s"><b>29</b><i>SA</i></li><li class="s"><b>30</b><i>SO</i></li>
    </ol></div>

    <div class="month"><h2>JULI</h2><ol>
      <li><b>1</b><i>MO</i><em>27</em></li><li><b>2</b><i>DI</i></li><li><b>3</b><i>MI</i></li><li><b>4</b><i>DO</i></li><li><b>5</b><i>FR</i></li><li class="s"><b>6</b><i>SA</i></li><li class="s"><b>7</b><i>SO</i></li>
      <li><b>8</b><i>MO</i><em>28</em></li><li><b>9</b><i>DI</i></li><li><b>10</b><i>MI</i></li><li><b>11</b><i>DO</i></li><li><b>12</b><i>FR</i></li><li class="s"><b>13</b><i>SA</i></li><li class="s"><b>14</b><i>SO</i></li>
      <li><b>15</b><i>MO</i><em>29</em></li><li><b>16</b><i>DI</i></li><li><b>17</b><i>MI</i></li><li><b>18</b><i>DO</i></li><li><b>19</b><i>FR</i></li><li class="s"><b>20</b><i>SA</i></li><li class="s"><b>21</b><i>SO</i></li>
      <li><b>22</b><i>MO</i><em>30</em></li><li><b>23</b><i>DI</i></li><li><b>24</b><i>MI</i></li><li><b>25</b><i>DO</i></li><li><b>26</b><i>FR</i></li><li class="s"><b>27</b><i>SA</i></li><li class="s"><b>28</b><i>SO</i></li>
      <li><b>29</b><i>MO</i><em>31</em></li><li><b>30</b><i>DI</i></li><li><b>31</b><i>MI</i></li>
    </ol></div>

    <div class="month"><h2>AUGUST</h2><ol>
      <li><b>1</b><i>DO</i></li><li><b>2</b><i>FR</i></li><li class="s"><b>3</b><i>SA</i></li><li class="s"><b>4</b><i>SO</i></li>
      <li><b>5</b><i>MO</i><em>32</em></li><li><b>6</b><i>DI</i></li><li><b>7</b><i>MI</i></li><li><b>8</b><i>DO</i></li><li><b>9</b><i>FR</i></li><li class="s"><b>10</b><i>SA</i></li><li class="s"><b>11</b><i>SO</i></li>
      <li><b>12</b><i>MO</i><em>33</em></li><li><b>13</b><i>DI</i></li><li><b>14</b><i>MI</i></li><li><b>15</b><i>DO</i></li><li><b>16</b><i>FR</i></li><li class="s"><b>17</b><i>SA</i></li><li class="s"><b>18</b><i>SO</i></li>
      <li><b>19</b><i>MO</i><em>34</em></li><li><b>20</b><i>DI</i></li><li><b>21</b><i>MI</i></li><li><b>22</b><i>DO</i></li><li><b>23</b><i>FR</i></li><li class="s"><b>24</b><i>SA</i></li><li class="s"><b>25</b><i>SO</i></li>
      <li><b>26</b><i>MO</i><em>35</em></li><li><b>27</b><i>DI</i></li><li><b>28</b><i>MI</i></li><li><b>29</b><i>DO</i></li><li><b>30</b><i>FR</i></li><li class="s"><b>31</b><i>SA</i></li>
    </ol></div>

    <div class="month"><h2>SEPTEMBER</h2><ol>
      <li class="s"><b>1</b><i>SO</i></li>
      <li><b>2</b><i>MO</i><em>36</em></li><li><b>3</b><i>DI</i></li><li><b>4</b><i>MI</i></li><li><b>5</b><i>DO</i></li><li><b>6</b><i>FR</i></li><li class="s"><b>7</b><i>SA</i></li><li class="s"><b>8</b><i>SO</i></li>
      <li><b>9</b><i>MO</i><em>37</em></li><li><b>10</b><i>DI</i></li><li><b>11</b><i>MI</i></li><li><b>12</b><i>DO</i></li><li><b>13</b><i>FR</i></li><li class="s"><b>14</b><i>SA</i></li><li class="s"><b>15</b><i>SO</i></li>
      <li><b>16</b><i>MO</i><em>38</em></li><li><b>17</b><i>DI</i></li><li><b>18</b><i>MI</i></li><li><b>19</b><i>DO</i></li><li><b>20</b><i>FR</i></li><li class="s"><b>21</b><i>SA</i></li><li class="s"><b>22</b><i>SO</i></li>
      <li><b>23</b><i>MO</i><em>39</em></li><li><b>24</b><i>DI</i></li><li><b>25</b><i>MI</i></li><li><b>26</b><i>DO</i></li><li><b>27</b><i>FR</i></li><li class="s"><b>28</b><i>SA</i></li><li class="s"><b>29</b><i>SO</i></li>
      <li><b>30</b><i>MO</i><em>40</em></li>
    </ol></div>

    <div class="month"><h2>OKTOBER</h2><ol>
      <li><b>1</b><i>DI</i></li><li><b>2</b><i>MI</i></li><li class="h"><b>3</b><i>DO · TAG DER DT. EINHEIT</i></li><li><b>4</b><i>FR</i></li><li class="s"><b>5</b><i>SA</i></li><li class="s"><b>6</b><i>SO</i></li>
      <li><b>7</b><i>MO</i><em>41</em></li><li><b>8</b><i>DI</i></li><li><b>9</b><i>MI</i></li><li><b>10</b><i>DO</i></li><li><b>11</b><i>FR</i></li><li class="s"><b>12</b><i>SA</i></li><li class="s"><b>13</b><i>SO</i></li>
      <li><b>14</b><i>MO</i><em>42</em></li><li><b>15</b><i>DI</i></li><li><b>16</b><i>MI</i></li><li><b>17</b><i>DO</i></li><li><b>18</b><i>FR</i></li><li class="s"><b>19</b><i>SA</i></li><li class="s"><b>20</b><i>SO</i></li>
      <li><b>21</b><i>MO</i><em>43</em></li><li><b>22</b><i>DI</i></li><li><b>23</b><i>MI</i></li><li><b>24</b><i>DO</i></li><li><b>25</b><i>FR</i></li><li class="s"><b>26</b><i>SA</i></li><li class="s"><b>27</b><i>SO</i></li>
      <li><b>28</b><i>MO</i><em>44</em></li><li><b>29</b><i>DI</i></li><li><b>30</b><i>MI</i></li><li><b>31</b><i>DO</i></li>
    </ol></div>

    <div class="month"><h2>NOVEMBER</h2><ol>
      <li><b>1</b><i>FR</i></li><li class="s"><b>2</b><i>SA</i></li><li class="s"><b>3</b><i>SO</i></li>
      <li><b>4</b><i>MO</i><em>45</em></li><li><b>5</b><i>DI</i></li><li><b>6</b><i>MI</i></li><li><b>7</b><i>DO</i></li><li><b>8</b><i>FR</i></li><li class="s"><b>9</b><i>SA</i></li><li class="s"><b>10</b><i>SO</i></li>
      <li><b>11</b><i>MO</i><em>46</em></li><li><b>12</b><i>DI</i></li><li><b>13</b><i>MI</i></li><li><b>14</b><i>DO</i></li><li><b>15</b><i>FR</i></li><li class="s"><b>16</b><i>SA</i></li><li class="s"><b>17</b><i>SO</i></li>
      <li><b>18</b><i>MO</i><em>47</em></li><li><b>19</b><i>DI</i></li><li><b>20</b><i>MI</i></li><li><b>21</b><i>DO</i></li><li><b>22</b><i>FR</i></li><li class="s"><b>23</b><i>SA</i></li><li class="s"><b>24</b><i>SO</i></li>
      <li><b>25</b><i>MO</i><em>48</em></li><li><b>26</b><i>DI</i></li><li><b>27</b><i>MI</i></li><li><b>28</b><i>DO</i></li><li><b>29</b><i>FR</i></li><li class="s"><b>30</b><i>SA</i></li>
    </ol></div>

    <div class="month"><h2>DEZEMBER</h2><ol>
      <li class="s"><b>1</b><i>SO</i></li>
      <li><b>2</b><i>MO</i><em>49</em></li><li><b>3</b><i>DI</i></li><li><b>4</b><i>MI</i></li><li><b>5</b><i>DO</i></li><li><b>6</b><i>FR</i></li><li class="s"><b>7</b><i>SA</i></li><li class="s"><b>8</b><i>SO</i></li>
      <li><b>9</b><i>MO</i><em>50</em></li><li><b>10</b><i>DI</i></li><li><b>11</b><i>MI</i></li><li><b>12</b><i>DO</i></li><li><b>13</b><i>FR</i></li><li class="s"><b>14</b><i>SA</i></li><li class="s"><b>15</b><i>SO</i></li>
      <li><b>16</b><i>MO</i><em>51</em></li><li><b>17</b><i>DI</i></li><li><b>18</b><i>MI</i></li><li><b>19</b><i>DO</i></li><li><b>20</b><i>FR</i></li><li class="s"><b>21</b><i>SA</i></li><li class="s"><b>22</b><i>SO</i></li>
      <li><b>23</b><i>MO</i><em>52</em></li><li><b>24</b><i>DI</i></li><li class="h"><b>25</b><i>MI · 1. WEIHNACHTSTAG</i></li><li class="h"><b>26</b><i>DO · 2. WEIHNACHTSTAG</i></li><li><b>27</b><i>FR</i></li><li class="s"><b>28</b><i>SA</i></li><li class="s"><b>29</b><i>SO</i></li>
      <li><b>30</b><i>MO</i><em>1</em></li><li><b>31</b><i>DI</i></li>
    </ol></div>
  </section>

  <footer class="footer">tel: 0431 – 552918-40 | info@dentora-fraese.de | www.dentora-fraese.de</footer>
</main>
</body>
</html>
```